Logo and business card design

I would like a logo and business card designed for a bookkeeping business called "Brightwell Accounting"
Would like the submission to be an editable file.

Info for business card:

Mara Lint, CPA, CGA
President
maralint@mailbox.example
555.301.8842
Lakemont, ON

```html
<!DOCTYPE html>
<html lang="en">
<head>
<meta charset="utf-8">
<title>Brightwell Accounting – Business Card</title>
<link href="https://fonts.googleapis.com/css2?family=Montserrat:wght@400;500;600;700&display=swap" rel="stylesheet">
<style>
  :root {
    --stage: #2b2b2d;
    --purple-deep: #4b1d6e;
    --purple: #6a2184;
    --magenta: #a0267f;
    --magenta-bright: #c2308f;
    --ink: #2a2a2e;
    --muted: #6b6b70;
    --paper: #ffffff;
  }
  * { margin: 0; padding: 0; box-sizing: border-box; }
  html, body {
    width: 1200px; height: 900px; overflow: hidden;
    background: var(--stage);
    font-family: "Montserrat", sans-serif;
  }
  .stage {
    position: relative; width: 1200px; height: 900px;
    display: flex; align-items: center; justify-content: center; gap: 50px;
  }
  .card {
    position: relative; width: 525px; height: 300px;
    border-radius: 20px; overflow: hidden;
    box-shadow: 0 12px 30px rgba(0,0,0,.45);
  }
  .card-art { position: absolute; inset: 0; }
  .card--front { background: linear-gradient(135deg, var(--purple) 0%, var(--magenta) 45%, var(--purple-deep) 100%); }
  .card--back { background: var(--paper); }

  .wordmark { position: absolute; display: flex; flex-direction: column; align-items: flex-start; font-weight: 700; line-height: 1.1; }
  .wordmark__dot { width: 40px; height: 40px; border-radius: 50%; margin-bottom: 10px; }
  .wordmark__name { font-size: 28px; letter-spacing: 1.5px; }
  .wordmark__sub { font-size: 11px; letter-spacing: 8px; margin-top: 2px; }

  .card--front .wordmark { left: 50%; top: 72px; transform: translateX(-50%); color: var(--paper); }
  .card--front .wordmark__dot { background: var(--paper); }

  .card--back .wordmark { left: 30px; top: 96px; color: var(--ink); }
  .card--back .wordmark__dot { width: 32px; height: 32px; background: var(--magenta); margin-bottom: 8px; }
  .card--back .wordmark__name { font-size: 21px; letter-spacing: 1px; }
  .card--back .wordmark__sub { font-size: 8.5px; letter-spacing: 5.6px; }

  .divider { position: absolute; left: 262px; top: 70px; width: 1.5px; height: 130px; background: var(--ink); }

  .contact { position: absolute; left: 278px; top: 66px; }
  .contact__name { color: var(--magenta); font-weight: 700; font-size: 17px; }
  .contact__role { color: var(--muted); font-size: 12px; margin-top: 2px; }
  .contact__list { list-style: none; margin-top: 30px; }
  .contact__item { display: flex; align-items: center; gap: 8px; font-size: 12px; color: var(--ink); margin-bottom: 6px; }
  .contact__icon { width: 13px; height: 13px; fill: var(--magenta); flex: none; }
</style>
</head>
<body>
<main class="stage">

  <section class="card card--front" aria-label="Card front">
    <svg class="card-art" viewBox="0 0 525 300" aria-hidden="true">
      <polygon points="0,276 120,276 135,262 525,262 525,300 0,300" fill="#ffffff"/>
      <polygon points="0,270 118,270 133,256 525,256 525,262 135,262 120,276 0,276" fill="#1e1a22"/>
      <polygon points="330,238 525,238 525,244 330,244" fill="#ffffff" opacity=".9"/>
    </svg>
    <div class="wordmark">
      <span class="wordmark__dot"></span>
      <span class="wordmark__name">BRIGHTWELL</span>
      <span class="wordmark__sub">ACCOUNTING</span>
    </div>
  </section>

  <section class="card card--back" aria-label="Card back">
    <svg class="card-art" viewBox="0 0 525 300" aria-hidden="true">
      <defs>
        <linearGradient id="band" x1="0" x2="1" y1="0" y2="0">
          <stop offset="0" stop-color="#a0267f"/>
          <stop offset="1" stop-color="#c2308f"/>
        </linearGradient>
      </defs>
      <polygon points="360,0 525,0 525,22 380,22" fill="url(#band)"/>
      <polygon points="0,0 350,0 342,6 0,6" fill="#1e1a22"/>
      <polygon points="0,258 150,258 170,236 330,236 330,242 175,242 155,264 0,264" fill="#a0267f" opacity=".35"/>
      <polygon points="0,264 155,264 175,242 330,242 312,300 0,300" fill="url(#band)"/>
      <polygon points="400,288 525,288 525,300 395,300" fill="#1e1a22"/>
    </svg>

    <div class="wordmark">
      <span class="wordmark__dot"></span>
      <span class="wordmark__name">BRIGHTWELL</span>
      <span class="wordmark__sub">ACCOUNTING</span>
    </div>

    <div class="divider"></div>

    <div class="contact">
      <p class="contact__name">Mara Lint, CPA, CGA</p>
      <p class="contact__role">President</p>
      <ul class="contact__list">
        <li class="contact__item">
          <svg class="contact__icon" viewBox="0 0 24 24" aria-hidden="true"><path d="M6.6 10.8a15.1 15.1 0 0 0 6.6 6.6l2.2-2.2a1 1 0 0 1 1-.25 11.4 11.4 0 0 0 3.6.57 1 1 0 0 1 1 1V20a1 1 0 0 1-1 1A17 17 0 0 1 3 4a1 1 0 0 1 1-1h3.5a1 1 0 0 1 1 1c0 1.250.2 2.45.57 3.57a1 1 0 0 1-.25 1z"/></svg>
          555.301.8842
        </li>
        <li class="contact__item">
          <svg class="contact__icon" viewBox="0 0 24 24" aria-hidden="true"><path d="M3 5h18v14H3z M3 5l9 7 9-7" fill="none" stroke="#a0267f" stroke-width="2.4"/></svg>
          maralint@mailbox.example
        </li>
        <li class="contact__item">
          <svg class="contact__icon" viewBox="0 0 24 24" aria-hidden="true"><path d="M12 2a7 7 0 0 0-7 7c0 5.2 7 13 7 13s7-7.8 7-13a7 7 0 0 0-7-7zm0 9.5A2.5 2.5 0 1 1 12 6.5a2.5 2.5 0 0 1 0 5z"/></svg>
          Lakemont, ON
        </li>
      </ul>
    </div>
  </section>

</main>
</body>
</html>
```